eJuice bottle label

We need a design for a label we are putting on eJuice liquid glass bottles, I have attached what we have in mind. We are a Colorado family ran business so we are going to name our flavors after Colorado Passes and would like a picture of the pass on the bottle. There will be 5 total labels.

```html
<!DOCTYPE html>
<html lang="en">
<head>
<meta charset="utf-8">
<title>High Ridge Premium Elixir – Bottle Labels</title>
<link rel="stylesheet" href="https://fonts.googleapis.com/css2?family=Kaushan+Script&family=Arimo:wght@400;700&display=swap">
<style>
  :root {
    --page: #ffffff;
    --ink: #15173c;
    --fine-print: #6b6b6b;
    --warning-red: #e0262b;
    --frame: #dcdcdc;

    --wolf-sky: #6ea3df;
    --wolf-mid: #a6aa52;
    --wolf-low: #56652f;
    --indep-sky: #eef4f4;
    --indep-mid: #a9bccb;
    --indep-low: #7f9a86;
    --lizard-sky: #9ea5d3;
    --lizard-mid: #b4a8bf;
    --lizard-low: #c8aa95;
    --love-sky: #e7f1fa;
    --love-mid: #b5c3d3;
    --love-low: #6a7876;
    --red-sky: #9fb5d7;
    --red-mid: #d4b9a5;
    --red-low: #6b6a4d;
  }
  html, body {
    margin: 0;
    padding: 0;
    width: 1000px;
    height: 1200px;
    overflow: hidden;
    background: var(--page);
  }
  .label-sheet {
    position: relative;
    width: 1000px;
    height: 1200px;
  }
  .label {
    position: absolute;
    left: 252px;
    width: 520px;
    height: 205px;
  }
  .ingredients {
    position: absolute;
    left: 2px;
    top: 2px;
    width: 58px;
    height: 203px;
    margin: 0;
    writing-mode: vertical-rl;
    font-family: "Arimo", Arial, sans-serif;
    font-size: 9.6px;
    letter-spacing: -0.3px;
    line-height: 13px;
    color: var(--fine-print);
    white-space: nowrap;
  }
  .ingredients strong { color: #333; }
  .pass-art {
    position: absolute;
    left: 73px;
    top: 0;
    width: 406px;
    height: 205px;
    outline: 1px solid var(--frame);
  }
  .pass-art .series-title {
    font-family: "Kaushan Script", cursive;
    font-size: 26px;
    fill: var(--ink);
  }
  .pass-art .pass-name {
    font-family: "Kaushan Script", cursive;
    font-size: 36px;
    fill: var(--ink);
    text-anchor: middle;
  }
  .pass-art .origin {
    font-family: "Kaushan Script", cursive;
    font-size: 19px;
    fill: var(--ink);
    text-anchor: middle;
  }
  .warning {
    position: absolute;
    left: 484px;
    top: 0;
    width: 34px;
    height: 205px;
  }
  .warning-text {
    position: absolute;
    left: 0;
    top: 0;
    width: 30px;
    height: 162px;
    margin: 0;
    writing-mode: vertical-rl;
    transform: rotate(180deg);
    font-family: "Arimo", Arial, sans-serif;
    font-size: 9.6px;
    letter-spacing: -0.3px;
    line-height: 15px;
    color: var(--fine-print);
    white-space: nowrap;
  }
  .no-minors {
    position: absolute;
    left: 1px;
    top: 168px;
    width: 26px;
    height: 26px;
  }
</style>
</head>
<body>
<main class="label-sheet">

  <section class="label" style="top:30px">
    <p class="ingredients"><strong>Ingredients:</strong> USP Vegetable Glycerin,<br>USP Propylene Glycol, Natural/Artificial<br>Flavours. May contain vaping grade<br>USP Nicotine.</p>
    <svg class="pass-art" viewBox="0 0 406 205">
      <defs>
        <linearGradient id="wolf-bg" x1="0" y1="0" x2="0" y2="1">
          <stop offset="0" style="stop-color:var(--wolf-sky)"/>
          <stop offset="0.35" style="stop-color:var(--wolf-sky)"/>
          <stop offset="0.55" style="stop-color:var(--wolf-mid)"/>
          <stop offset="1" style="stop-color:var(--wolf-low)"/>
        </linearGradient>
        <path id="arc-1" d="M28 84 Q203 18 378 84"/>
      </defs>
      <rect width="406" height="205" fill="url(#wolf-bg)" role="img" aria-label="Landscape of Wolf Creek Pass: forested valley and meadow under a blue sky"/>
      <text class="series-title"><textPath href="#arc-1" startOffset="50%" text-anchor="middle">High Ridge Premium Elixir</textPath></text>
      <text class="pass-name" x="203" y="120">Wolf Creek Pass</text>
      <text class="origin" x="203" y="182">Hand Crafted in Colorado</text>
    </svg>
    <div class="warning">
      <p class="warning-text">May contain nicotine.<br>Keep away from Children &amp; Pets.</p>
      <svg class="no-minors" viewBox="0 0 26 26" role="img" aria-label="Not for minors">
        <circle cx="13" cy="13" r="10.5" fill="#fff" stroke="var(--warning-red)" stroke-width="2.5"/>
        <line x1="5.6" y1="20.4" x2="20.4" y2="5.6" stroke="var(--warning-red)" stroke-width="2.5"/>
      </svg>
    </div>
  </section>

  <section class="label" style="top:262px">
    <p class="ingredients"><strong>Ingredients:</strong> USP Vegetable Glycerin,<br>USP Propylene Glycol, Natural/Artificial<br>Flavours. May contain vaping grade<br>USP Nicotine.</p>
    <svg class="pass-art" viewBox="0 0 406 205">
      <defs>
        <linearGradient id="indep-bg" x1="0" y1="0" x2="0" y2="1">
          <stop offset="0" style="stop-color:var(--indep-sky)"/>
          <stop offset="0.4" style="stop-color:var(--indep-mid)"/>
          <stop offset="1" style="stop-color:var(--indep-low)"/>
        </linearGradient>
        <path id="arc-2" d="M28 84 Q203 18 378 84"/>
      </defs>
      <rect width="406" height="205" fill="url(#indep-bg)" role="img" aria-label="Landscape of Independence Pass: misty glacial valley between mountain slopes"/>
      <text class="series-title"><textPath href="#arc-2" startOffset="50%" text-anchor="middle">High Ridge Premium Elixir</textPath></text>
      <text class="pass-name" x="203" y="120">Independence Pass</text>
      <text class="origin" x="203" y="182">Hand Crafted in Colorado</text>
    </svg>
    <div class="warning">
      <p class="warning-text">May contain nicotine.<br>Keep away from Children &amp; Pets.</p>
      <svg class="no-minors" viewBox="0 0 26 26" role="img" aria-label="Not for minors">
        <circle cx="13" cy="13" r="10.5" fill="#fff" stroke="var(--warning-red)" stroke-width="2.5"/>
        <line x1="5.6" y1="20.4" x2="20.4" y2="5.6" stroke="var(--warning-red)" stroke-width="2.5"/>
      </svg>
    </div>
  </section>

  <section class="label" style="top:490px">
    <p class="ingredients"><strong>Ingredients:</strong> USP Vegetable Glycerin,<br>USP Propylene Glycol, Natural/Artificial<br>Flavours. May contain vaping grade<br>USP Nicotine.</p>
    <svg class="pass-art" viewBox="0 0 406 205">
      <defs>
        <linearGradient id="lizard-bg" x1="0" y1="0" x2="0" y2="1">
          <stop offset="0" style="stop-color:var(--lizard-sky)"/>
          <stop offset="0.5" style="stop-color:var(--lizard-mid)"/>
          <stop offset="1" style="stop-color:var(--lizard-low)"/>
        </linearGradient>
        <path id="arc-3" d="M28 84 Q203 18 378 84"/>
      </defs>
      <rect width="406" height="205" fill="url(#lizard-bg)" role="img" aria-label="Landscape of Lizard Head Pass: rocky spire peak under a lavender sky"/>
      <text class="series-title"><textPath href="#arc-3" startOffset="50%" text-anchor="middle">High Ridge Premium Elixir</textPath></text>
      <text class="pass-name" x="203" y="120">Lizard Head Pass</text>
      <text class="origin" x="203" y="182">Hand Crafted in Colorado</text>
    </svg>
    <div class="warning">
      <p class="warning-text">May contain nicotine.<br>Keep away from Children &amp; Pets.</p>
      <svg class="no-minors" viewBox="0 0 26 26" role="img" aria-label="Not for minors">
        <circle cx="13" cy="13" r="10.5" fill="#fff" stroke="var(--warning-red)" stroke-width="2.5"/>
        <line x1="5.6" y1="20.4" x2="20.4" y2="5.6" stroke="var(--warning-red)" stroke-width="2.5"/>
      </svg>
    </div>
  </section>

  <section class="label" style="top:718px">
    <p class="ingredients"><strong>Ingredients:</strong> USP Vegetable Glycerin,<br>USP Propylene Glycol, Natural/Artificial<br>Flavours. May contain vaping grade<br>USP Nicotine.</p>
    <svg class="pass-art" viewBox="0 0 406 205">
      <defs>
        <linearGradient id="love-bg" x1="0" y1="0" x2="0" y2="1">
          <stop offset="0" style="stop-color:var(--love-sky)"/>
          <stop offset="0.4" style="stop-color:var(--love-mid)"/>
          <stop offset="1" style="stop-color:var(--love-low)"/>
        </linearGradient>
        <path id="arc-4" d="M28 84 Q203 18 378 84"/>
      </defs>
      <rect width="406" height="205" fill="url(#love-bg)" role="img" aria-label="Landscape of Loveland Pass: snowy ridges and a winding road under a pale cloudy sky"/>
      <text class="series-title"><textPath href="#arc-4" startOffset="50%" text-anchor="middle">High Ridge Premium Elixir</textPath></text>
      <text class="pass-name" x="203" y="120">Loveland Pass</text>
      <text class="origin" x="203" y="182">Hand Crafted in Colorado</text>
    </svg>
    <div class="warning">
      <p class="warning-text">May contain nicotine.<br>Keep away from Children &amp; Pets.</p>
      <svg class="no-minors" viewBox="0 0 26 26" role="img" aria-label="Not for minors">
        <circle cx="13" cy="13" r="10.5" fill="#fff" stroke="var(--warning-red)" stroke-width="2.5"/>
        <line x1="5.6" y1="20.4" x2="20.4" y2="5.6" stroke="var(--warning-red)" stroke-width="2.5"/>
      </svg>
    </div>
  </section>

  <section class="label" style="top:946px">
    <p class="ingredients"><strong>Ingredients:</strong> USP Vegetable Glycerin,<br>USP Propylene Glycol, Natural/Artificial<br>Flavours. May contain vaping grade<br>USP Nicotine.</p>
    <svg class="pass-art" viewBox="0 0 406 205">
      <defs>
        <linearGradient id="red-bg" x1="0" y1="0" x2="0" y2="1">
          <stop offset="0" style="stop-color:var(--red-sky)"/>
          <stop offset="0.3" style="stop-color:var(--red-sky)"/>
          <stop offset="0.55" style="stop-color:var(--red-mid)"/>
          <stop offset="1" style="stop-color:var(--red-low)"/>
        </linearGradient>
        <path id="arc-5" d="M28 84 Q203 18 378 84"/>
      </defs>
      <rect width="406" height="205" fill="url(#red-bg)" role="img" aria-label="Landscape of Red Mountain Pass: rust-coloured peaks and forest under a blue sky"/>
      <text class="series-title"><textPath href="#arc-5" startOffset="50%" text-anchor="middle">High Ridge Premium Elixir</textPath></text>
      <text class="pass-name" x="203" y="120">Red Mountain Pass</text>
      <text class="origin" x="203" y="182">Hand Crafted in Colorado</text>
    </svg>
    <div class="warning">
      <p class="warning-text">May contain nicotine.<br>Keep away from Children &amp; Pets.</p>
      <svg class="no-minors" viewBox="0 0 26 26" role="img" aria-label="Not for minors">
        <circle cx="13" cy="13" r="10.5" fill="#fff" stroke="var(--warning-red)" stroke-width="2.5"/>
        <line x1="5.6" y1="20.4" x2="20.4" y2="5.6" stroke="var(--warning-red)" stroke-width="2.5"/>
      </svg>
    </div>
  </section>

</main>
</body>
</html>
```